Vision, Mission and Culture Posters

We have written text paragraphs for our company vision and mission and need them made into a2 or a3 sized posters using our logo for inspiration for colour. Our company culture has 10 paragraphs and we'd like this to be a single poster of a2 or a1. Each poster should have the logo on and share common design. It's not a complex job really.

Industry/Entity Type

It Company

Requirements
Nice to have
• These will be going up on our office wall so need to be clear to read from a distance and look professional but also not stodgy.

```html
<!DOCTYPE html>
<html lang="en">
<head>
<meta charset="utf-8">
<title>Kerbside Bay Hire – Company Values</title>
<link href="https://fonts.googleapis.com/css2?family=Oswald:wght@500;700&family=Open+Sans:wght@400;600&display=swap" rel="stylesheet">
<style>
  :root {
    --orange: #f26b1d;
    --orange-deep: #e0520f;
    --amber: #f9a21b;
    --cream: #fff8ec;
    --white: #ffffff;
    --ink: #3a3a3a;
    --red: #d8262d;
  }
  * { box-sizing: border-box; margin: 0; padding: 0; }
  html, body { width: 849px; height: 1200px; overflow: hidden; }
  body {
    background: radial-gradient(circle at 50% 40%, var(--amber) 0%, var(--orange) 55%, var(--orange-deep) 100%);
    font-family: "Open Sans", Arial, sans-serif;
    color: var(--ink);
    position: relative;
  }
  .poster-title {
    height: 96px;
    display: flex;
    flex-direction: column;
    justify-content: center;
    align-items: center;
    color: var(--white);
    font-family: "Oswald", "Arial Narrow", sans-serif;
    font-weight: 700;
    font-size: 38px;
    line-height: 1.05;
    letter-spacing: 1px;
    text-transform: uppercase;
  }
  .values-panel {
    position: absolute;
    left: 14px; right: 14px; top: 96px; bottom: 14px;
    background: linear-gradient(180deg, var(--white) 0%, var(--cream) 100%);
    display: flex;
    gap: 22px;
    padding: 14px 18px 18px;
  }
  .values-column {
    flex: 1;
    display: flex;
    flex-direction: column;
    justify-content: space-between;
  }
  .brand-block {
    display: flex;
    align-items: center;
    gap: 12px;
    width: 270px;
    height: 104px;
    border: 3px solid var(--red);
    border-radius: 10px;
    background: var(--white);
    padding: 0 18px;
  }
  .brand-mark {
    width: 22px; height: 22px;
    background: var(--red);
    flex: none;
  }
  .brand-name {
    font-family: "Open Sans", Arial, sans-serif;
    font-weight: 600;
    font-size: 26px;
    line-height: 1.1;
    color: var(--red);
  }
  .value-heading {
    display: inline-block;
    background: var(--orange);
    color: var(--white);
    font-family: "Oswald", "Arial Narrow", sans-serif;
    font-weight: 500;
    font-size: 17px;
    letter-spacing: 0.5px;
    text-transform: uppercase;
    padding: 2px 26px 2px 10px;
    clip-path: polygon(0 0, 100% 0, calc(100% - 14px) 100%, 0 100%);
    margin-bottom: 6px;
  }
  .value-section { border-top: 2px solid var(--orange); padding-top: 0; }
  .value-text {
    font-size: 12px;
    line-height: 1.5;
    text-align: justify;
  }
</style>
</head>
<body>
  <header class="poster-title">
    <span>Kerbside Bay Hire</span>
    <span>Company Values</span>
  </header>

  <main class="values-panel">
    <div class="values-column">
      <div class="brand-block">
        <span class="brand-mark"></span>
        <span class="brand-name">Kerbside Bay Hire</span>
      </div>

      <section class="value-section">
        <h2 class="value-heading">Communication</h2>
        <p class="value-text">We believe in open communication, giving customers, colleagues and partners honest, accurate, concise and prompt information relevant to their needs. We listen carefully, ask questions when unsure and share ideas freely. Polite, friendly and warm contact builds trust and keeps every conversation clear and useful for everyone involved.</p>
      </section>

      <section class="value-section">
        <h2 class="value-heading">Education</h2>
        <p class="value-text">We believe in continual learning and education, and we thrive on helping colleagues grow by sharing knowledge and experience. Mistakes are lessons, not failures. Everyone learns differently, so we adapt how we teach and challenge one another to keep improving in a way that suits each person.</p>
      </section>

      <section class="value-section">
        <h2 class="value-heading">Professionalism</h2>
        <p class="value-text">We represent ourselves as professionals and our business to the best of our ability at all times. First impressions matter, so we treat every customer with courtesy, whether by phone, email or in person. We are always on time, well presented and prepared for the task at hand.</p>
      </section>

      <section class="value-section">
        <h2 class="value-heading">Ownership</h2>
        <p class="value-text">We are each fully responsible for our roles and for our contribution to the success of the business. We are accountable for our results, our ability to improve and what we do. We own our mistakes and fix them quickly.</p>
      </section>

      <section class="value-section">
        <h2 class="value-heading">Commercial Awareness</h2>
        <p class="value-text">We understand that in a small business everything we do can affect the success of the company, so we commit ourselves to thinking about the impact of our choices. Every decision should serve the customer and the business, weighing cost against real value. Greater benefit for our customers means lasting growth for us all.</p>
      </section>
    </div>

    <div class="values-column">
      <section class="value-section">
        <h2 class="value-heading">Balance</h2>
        <p class="value-text">We try to find the best balance in our lives between our responsibilities, obligations, duties and desires while still ensuring we have time to devote to friends, families, fun and life. We try to balance our opinions with those of others and believe that this balance creates fairness, integrity, self-control and a great attitude.</p>
      </section>

      <section class="value-section">
        <h2 class="value-heading">Customer Service</h2>
        <p class="value-text">We believe that without our customers we would not be successful, and we understand that the level of service we give is critical to our continued growth. Even the smallest action should show care and attention. We go out of our way to help any customer with an issue and are only satisfied when they leave happy.</p>
      </section>

      <section class="value-section">
        <h2 class="value-heading">Consistency</h2>
        <p class="value-text">We believe in consistency of our work, our approach, our positive attitude and our actions, holding ourselves to a standard that colleagues and customers can rely on. A steady, familiar way of working builds the trust that strengthens every relationship we have.</p>
      </section>

      <section class="value-section">
        <h2 class="value-heading">Success</h2>
        <p class="value-text">We understand success isn't given; it is earned every day, piece by piece. We strive to succeed as individuals and as a team, and we support each other in earning that success. We celebrate achievements, large and small, and reward hard work and dedication.</p>
      </section>

      <section class="value-section">
        <h2 class="value-heading">Commitment</h2>
        <p class="value-text">We are committed to the company vision, its mission and to upholding the company culture as well as sharing it with new colleagues. We talk about our values, mission and culture often, and we help one another live by them. We are not afraid to tell colleagues when we feel they are not showing the right commitment, always in a positive and helpful way.</p>
      </section>
    </div>
  </main>
</body>
</html>
```